Business card for Tolvery Anesthesia LLC

This is for a business care for Tolvery Anesthesia LLC. Dr. Lisbeth Tolvery, CRNA, DNAP is the sole provider in the LLC. Business address is 4718 N Brackley Street,
Oakhaven, PA 17342
CRNA stands for certified registered nurse anesthetist
"Keeping you safe and comfortable"
I plan to give this business card to the patients that I provide anesthesia to.
Creative design that ties into Anesthesia. Calm soothing colors.

Target Market(s)

Business card for my patients.

Industry/Entity Type

Medicine

Contact Information for Business Card

Creative, professional, eye catching

Logo Text

Tolvery Anesthesia

Font styles to use
Serif
Script

Colors

Designer to choose colors to be used in the design.

Requirements
Must have
• Tolvery Anesthesia
• Dr. Lisbeth Tolvery, CRNA, DNAP
• tolvery.anesthesia@ quillmail.net
Nice to have
• "Keeping you safe and comfortable"
Should not have
• phone number

```html
<!DOCTYPE html>
<html lang="en">
<head>
<meta charset="utf-8">
<title>Tolvery Anesthesia LLC — Business Card</title>
<link rel="stylesheet" href="https://fonts.googleapis.com/css2?family=Lato:wght@400;700&display=swap">
<style>
  :root {
    --backdrop: #3a3431;
    --card: #0d0d0e;
    --card-edge: #1c1c1e;
    --green: #6aaa2a;
    --blue: #3d6ea8;
    --white: #e9e9e9;
    --silver: #c9c9cb;
  }
  * { box-sizing: border-box; margin: 0; padding: 0; }
  html, body {
    width: 1200px;
    height: 844px;
    overflow: hidden;
    background: var(--backdrop);
    font-family: "Lato", Arial, sans-serif;
  }
  .sheet {
    width: 1200px;
    height: 844px;
    display: flex;
    align-items: center;
    justify-content: center;
    gap: 40px;
  }
  .card {
    position: relative;
    width: 540px;
    height: 309px;
    background: var(--card);
    border: 1px solid var(--card-edge);
    box-shadow: 0 10px 30px rgba(0,0,0,0.45);
  }
  .brand {
    display: flex;
    align-items: center;
    gap: 12px;
    font-weight: 400;
    text-transform: uppercase;
    letter-spacing: 0.06em;
    line-height: 1.15;
  }
  .brand-dot {
    flex: none;
    width: 34px;
    height: 34px;
    border-radius: 50%;
  }
  .brand-name { display: block; }

  /* front */
  .card-front .brand {
    position: absolute;
    top: 52px;
    right: 40px;
    color: var(--blue);
    font-size: 22px;
    text-align: right;
  }
  .card-front .brand-dot { background: var(--blue); }
  .contact {
    position: absolute;
    left: 40px;
    bottom: 40px;
    color: var(--white);
    font-size: 14px;
    line-height: 1.65;
  }
  .contact-name {
    color: var(--green);
    font-weight: 700;
    font-size: 19px;
    text-transform: uppercase;
    letter-spacing: 0.01em;
  }
  .contact-name .credentials {
    font-weight: 400;
    font-size: 13px;
  }
  .contact-address { margin-top: 8px; }
  .tagline {
    margin-top: 10px;
    color: var(--green);
    text-transform: uppercase;
    font-size: 14px;
    letter-spacing: 0.03em;
  }

  /* back */
  .card-back {
    display: flex;
    align-items: center;
    justify-content: center;
  }
  .card-back .brand {
    color: var(--silver);
    font-size: 24px;
    flex-direction: column;
    text-align: center;
  }
  .card-back .brand-dot {
    width: 52px;
    height: 52px;
    background: var(--silver);
  }
</style>
</head>
<body>
  <main class="sheet">
    <section class="card card-front" aria-label="Card front">
      <div class="brand">
        <span class="brand-dot" aria-hidden="true"></span>
        <span class="brand-name">Tolvery<br>Anesthesia LLC</span>
      </div>
      <div class="contact">
        <p class="contact-name">Dr. Lisbeth Tolvery, <span class="credentials">CRNA, DNAP</span></p>
        <p class="contact-email">tolvery.anesthesia@quillmail.net</p>
        <p class="contact-address">4718 N Brackley Street, Oakhaven, PA 17342</p>
        <p class="tagline">Keeping you safe and comfortable</p>
      </div>
    </section>

    <section class="card card-back" aria-label="Card back">
      <div class="brand">
        <span class="brand-dot" aria-hidden="true"></span>
        <span class="brand-name">Tolvery<br>Anesthesia LLC</span>
      </div>
    </section>
  </main>
</body>
</html>
```